Vanta Roving Car Wash and Detail Services, 'needs a logo and card design'

I need a logo and Card design for a new company based in Perth Western Australia called, 'Vanta Roving Car Wash and Detail Services'. I want to offer a mobile car wash and detail service across all the Perth metropolitan areas at lower prices, and offer more reliability. I would like to see designs with colours such as red, white, and black. The final design should communicate trust reliability and confidence in the services I can provide. The card must include my first name 'Ormand' and my mobile number '0417208364' for an obligation free quote.

Target Market(s)

Aimed at anyone who owns and drives a motor vehicle.

Industry/Entity Type

It Company

Contact Information for Business Card

Business Name'Vanta Roving Car Wash and Detail Services', My first name 'Ormand', and my mobile phone '0417208364' for an obligation free quote.

Font styles to use
Serif
Decorative
Script

Colors
ffffff
000000
d3d3d3
ec1f27
7f7f7f

Requirements
Must have
• Business Name'Vanta Roving Car Wash and Detail Services', My first name 'Ormand', and my mobile phone '0417208364' for an obligation free quote.
• Logo design
Nice to have
• A slogan, such as 'I come to you, and wash your car wherever you are' to let customers know I am at their service.
• Car design 'shine and clean feeling'

```html
<!DOCTYPE html>
<html lang="en">
<head>
<meta charset="utf-8">
<title>Vanta Roving Car Wash and Detail Services – Business Card</title>
<link rel="stylesheet" href="https://fonts.googleapis.com/css2?family=Montserrat:wght@700&family=Roboto:wght@300;400&display=swap">
<style>
  :root {
    --red: #ec1f27;
    --black: #231f20;
    --white: #ffffff;
    --backdrop: #d3d3d3;
    --grey: #7f7f7f;
  }
  * { margin: 0; padding: 0; box-sizing: border-box; }
  html, body {
    width: 1200px;
    height: 826px;
    overflow: hidden;
    background: var(--backdrop);
  }
  .card {
    position: absolute;
    left: 100px;
    top: 109px;
    width: 1000px;
    height: 608px;
    background: var(--white);
    overflow: hidden;
    box-shadow: 4px 6px 12px rgba(0,0,0,0.35);
  }
  .corner-swoosh {
    position: absolute;
    left: 0;
    top: 0;
  }
  .brand {
    position: absolute;
    left: 360px;
    top: 46px;
    display: flex;
    align-items: center;
    gap: 22px;
  }
  .brand-mark {
    width: 112px;
    height: 112px;
    border-radius: 50%;
    border: 8px solid var(--red);
    flex: none;
  }
  .brand-name {
    font-family: "Montserrat", sans-serif;
    font-weight: 700;
    color: var(--black);
    line-height: 1.1;
  }
  .brand-name .primary {
    display: block;
    font-size: 54px;
    letter-spacing: 0.5px;
    text-transform: uppercase;
  }
  .brand-name .secondary {
    display: block;
    font-size: 26px;
    margin-top: 6px;
  }
  .contact-name {
    position: absolute;
    left: 74px;
    top: 372px;
    font-family: "Montserrat", sans-serif;
    font-weight: 700;
    font-size: 44px;
    color: var(--black);
  }
  .contact-line {
    position: absolute;
    left: 74px;
    top: 446px;
    display: flex;
    align-items: center;
    font-family: "Roboto", sans-serif;
    color: var(--black);
  }
  .phone-icon { width: 30px; height: 50px; margin-right: 20px; }
  .phone-number {
    font-weight: 300;
    font-size: 46px;
    margin-right: 36px;
  }
  .quote-note {
    font-weight: 400;
    font-size: 33px;
  }
  .slogan-band {
    position: absolute;
    left: 0;
    bottom: 0;
    width: 100%;
    height: 67px;
    background: var(--black);
    color: var(--white);
    font-family: "Montserrat", sans-serif;
    font-weight: 700;
    font-size: 28px;
    display: flex;
    align-items: center;
    justify-content: center;
  }
</style>
</head>
<body>
  <div class="card">
    <svg class="corner-swoosh" width="380" height="360" viewBox="0 0 380 360" aria-hidden="true">
      <path d="M0 0 H365 C210 55 70 170 0 348 Z" fill="var(--red)"/>
    </svg>

    <div class="brand">
      <div class="brand-mark"></div>
      <div class="brand-name">
        <span class="primary">Vanta Roving</span>
        <span class="secondary">Car Wash and Detail Services</span>
      </div>
    </div>

    <div class="contact-name">Ormand</div>

    <div class="contact-line">
      <svg class="phone-icon" viewBox="0 0 30 50" aria-hidden="true">
        <rect x="2" y="2" width="26" height="46" rx="6" fill="var(--red)"/>
        <rect x="7" y="9" width="16" height="14" rx="2" fill="var(--white)"/>
        <circle cx="15" cy="36" r="4" fill="var(--white)"/>
      </svg>
      <span class="phone-number">0417208364</span>
      <span class="quote-note">call for an obligation free quote</span>
    </div>

    <div class="slogan-band">I come to you, and wash your car wherever you are</div>
  </div>
</body>
</html>
```